Qorvex app promo Web page

Vantel Forge Project Description / Qorvex App Website

Project: Website / Basic / For an Qorvex app promo with a company logo revision

Purpose: Provide a public “Face” for a new Qorvex app, promoting the app and having a link to the Brimzo store.

Depth: 2 levels: Level 1 - Home page / Level 2: Media, Contact, About, Blog (all 1-page) (5 pages in all)(Button pages will be similar and simple.

Navigation: Home page: Button: Brimzo store link, Media, Contact, About, Blog

Design style: The Web design can go one of two ways - directly reflect the app Style design or have a clean, dramatic, “European” design with a white or black background. The second approach is probably the best way, as we may use this website to feature other apps as well.

Home page: See attached page with elements for design of art / copy / buttons. Also, I attach some app web pages that can help inform the designer's appreciation for what we want.

Media Page See attached rough layout of art

Contact See attached file

About See attached file

Blog See attached file

Reason: I am traveling and need to review everyone's work more extensively plan to co,plete and decide over the weekend. .

Reason: My business trip was extended - need the time to review designs with my partner.I will send feedback to designers, though - later tonight.

Target Market(s)

Adults with smart phones (Aged 18-45) & media visitors

Industry/Entity Type

Store

Requirements
Must have
• Attached information on page contents...

Home page:
- Company logo
- Qorvex app icon and name
- Product description
- Features list
- Button to go to Brimzo Store
- Buttons to go to other pages: Media, Contact, About, Blog

Media page:
- Company logo
- List of media downloads (Releases, backgrounder, etc.)
- Return to home button

Contact page:
- Company logo
- E-mail structure for inputting name, e-mail, and message

About:
- Company logo
- Space for copy on company / and app

Blog:
- Company logo
- Space for blog to appear

Nice to have
• I have attached a few other site designs to show the elegance and strong design we would like.

We do have a company logo approach that will need to be tweaked a bit.

I would like to see a clean design that allows the app to be featured but will be distinctive in its own right. We want to be seen as a very contemporary, clean, sleek, elegant design type company.
Should not have
• Not too cluttered of a design.

```html
<!DOCTYPE html>
<html lang="en">
<head>
<meta charset="utf-8">
<title>Contact – Varno Health Resources, LLC</title>
<link href="https://fonts.googleapis.com/css2?family=Source+Sans+3:wght@400;600;700&display=swap" rel="stylesheet">
<style>
  :root {
    --page-bg: #e6e6e6;
    --topbar: #3e3e3e;
    --panel: #ffffff;
    --ink: #222222;
    --nav-ink: #666666;
    --accent-red: #cc1f1f;
    --brand-green: #7dc242;
    --form-bg: #d9d9d9;
    --field-bg: #ffffff;
    --placeholder: #a8a8a8;
    --banner-dark: #111111;
    --banner-mid: #3a3a3a;
    --social: #1b8fd8;
    --social-edge: #0f6fae;
    --footer: #363636;
    --footer-base: #232323;
    --footer-ink: #ffffff;
    --app-red: #8e1012;
  }
  * { box-sizing: border-box; margin: 0; padding: 0; }
  html, body { width: 1200px; height: 813px; overflow: hidden; }
  body {
    position: relative;
    background: var(--page-bg);
    font-family: "Source Sans 3", "Myriad Pro", sans-serif;
    color: var(--ink);
  }
  .topbar { position: absolute; left: 0; top: 0; width: 1200px; height: 14px; background: var(--topbar); }

  .brand { position: absolute; left: 178px; top: 26px; display: flex; align-items: center; gap: 9px; }
  .brand-dot { width: 44px; height: 44px; border-radius: 50%; background: var(--brand-green); }
  .brand-name { font-size: 21px; font-weight: 400; color: var(--ink); letter-spacing: -0.2px; }

  .main-nav { position: absolute; left: 555px; top: 32px; display: flex; height: 42px; border-left: 1px dotted #c4c4c4; }
  .main-nav a {
    width: 91px; height: 42px; display: flex; align-items: center; padding-left: 6px;
    border-right: 1px dotted #c4c4c4; font-size: 12px; font-weight: 700; color: var(--nav-ink);
    text-decoration: none; text-transform: uppercase;
  }
  .main-nav a::before { content: "›"; font-size: 16px; margin-right: 3px; line-height: 1; position: relative; top: -1px; }
  .main-nav a.is-current { color: #000; }
  .main-nav a.is-current::before { color: var(--accent-red); }

  .panel { position: absolute; left: 170px; top: 88px; width: 857px; height: 546px; background: var(--panel); }

  .contact-photo {
    position: absolute; left: 189px; top: 137px; width: 305px; height: 82px;
    background: linear-gradient(90deg, #d8c9a6 0%, #efe6d0 30%, #3b3934 50%, #e6dcc4 72%, #c9b48f 100%);
  }
  .app-card { position: absolute; left: 200px; top: 234px; display: flex; gap: 13px; }
  .app-icon { width: 61px; height: 60px; border-radius: 8px; background: var(--app-red); }
  .app-name { font-size: 20px; font-weight: 700; margin-top: 2px; }
  .app-email { font-size: 14px; margin-top: 8px; }

  .banner {
    position: absolute; left: 513px; top: 137px; width: 498px; height: 82px;
    background: linear-gradient(90deg, var(--banner-mid) 0%, var(--banner-dark) 100%);
    display: flex; align-items: center; gap: 11px; padding-left: 21px;
  }
  .banner .brand-dot { width: 58px; height: 58px; }
  .banner .brand-name { font-size: 26px; color: #fff; }

  .contact-form { position: absolute; left: 514px; top: 237px; width: 496px; height: 382px; background: var(--form-bg); }
  .field {
    position: absolute; left: 23px; width: 162px; height: 25px; background: var(--field-bg);
    border: none; font: 400 15px "Source Sans 3", sans-serif; color: var(--ink); padding: 4px 9px 0;
  }
  .field::placeholder { color: var(--placeholder); }
  .field-name { top: 65px; }
  .field-email { top: 96px; }
  .field-subject { top: 126px; }
  .field-message { position: absolute; left: 196px; top: 64px; width: 223px; height: 188px; border: none; background: var(--field-bg); resize: none; font: 400 14px "Source Sans 3", sans-serif; padding: 8px; }

  .social { position: absolute; left: 1027px; top: 111px; display: flex; flex-direction: column; gap: 2px; }
  .social a {
    display: flex; align-items: center; justify-content: center; width: 27px; color: #fff;
    background: var(--social); border-radius: 0 5px 5px 0;
    box-shadow: 1px 1px 0 var(--social-edge);
    font-size: 11px; font-weight: 700; letter-spacing: 0.3px; line-height: 1;
    text-decoration: none; writing-mode: vertical-rl; transform: rotate(180deg);
  }
  .social .tab-linkly { height: 50px; border-radius: 5px 0 0 5px; }
  .social .tab-chirpo { height: 38px; border-radius: 5px 0 0 5px; }

  .site-footer { position: absolute; left: 0; top: 656px; width: 1200px; height: 122px; background: var(--footer); }
  .footer-nav { position: absolute; left: 199px; top: 10px; display: flex; flex-direction: column; gap: 5px; }
  .footer-nav a { color: var(--footer-ink); font-size: 12px; font-weight: 700; text-decoration: none; line-height: 17.3px; }
  .copyright {
    position: absolute; left: 0; top: 778px; width: 1200px; height: 35px; background: var(--footer-base);
    border-top: 1px solid #444; color: var(--footer-ink); font-size: 10.5px; text-align: center; line-height: 34px;
  }
</style>
</head>
<body>
  <div class="topbar"></div>

  <header>
    <div class="brand">
      <span class="brand-dot"></span>
      <span class="brand-name">Varno Health Resources, LLC</span>
    </div>
    <nav class="main-nav">
      <a href="#">Home</a>
      <a href="#">About</a>
      <a href="#">Media</a>
      <a href="#">Blog</a>
      <a href="#" class="is-current">Contact</a>
    </nav>
  </header>

  <main class="panel"></main>

  <div class="contact-photo" role="img" aria-label="Photo of a vintage black rotary telephone on a table"></div>

  <div class="app-card">
    <div class="app-icon"></div>
    <div>
      <div class="app-name">Heartly™</div>
      <div class="app-email">hello@heartly-mail.com</div>
    </div>
  </div>

  <div class="banner">
    <span class="brand-dot"></span>
    <span class="brand-name">Varno Health Resources, LLC</span>
  </div>

  <form class="contact-form">
    <input class="field field-name" type="text" placeholder="Name">
    <input class="field field-email" type="email" placeholder="Email">
    <input class="field field-subject" type="text" placeholder="Subject">
    <textarea class="field-message" aria-label="Message"></textarea>
  </form>

  <div class="social">
    <a href="#" class="tab-linkly">Linkly</a>
    <a href="#" class="tab-chirpo">Chirpo</a>
  </div>

  <footer class="site-footer">
    <nav class="footer-nav">
      <a href="#">Home</a>
      <a href="#">About</a>
      <a href="#">Media</a>
      <a href="#">Blog</a>
      <a href="#">Contact</a>
    </nav>
  </footer>
  <div class="copyright">© Copyright 2013 . All rights reserved&nbsp; Varno Health Resources, LLC.</div>
</body>
</html>
```